I need a book cover design for my book "Roaming Quartets." It is a non-fiction book focused on answering the question of whether American evangelicals look more like the Quartets than Jesus.

The subtitle is "The Curious Habits of Norway's Traveling Fiddlers and Their Seaside Rivals." The author name is Dorian Whitlock.

I will be publishing this as an ebook and paperback.

I am open to all ideas, but will share the only thought I had as a possible design. In the title, the third letter in both words is "A." I thought about the idea of having the "A" in "Roaming" have a halo and the "A" in "Quartets" somehow seem to be a shadow of that first "A" but have devil horns instead of a halo. Again, I'm not sold on that, but am sharing it as one design possibility.

I am not interested in the book cover design having a cheesy religious look to it (as many do). I am more interested in it looking like a professional non-fiction cover.

```html
<!DOCTYPE html>
<html lang="en">
<head>
<meta charset="UTF-8">
<title>Roaming Quartets — Book Cover</title>
<link rel="stylesheet" href="https://fonts.googleapis.com/css2?family=Oswald:wght@400;600&family=Crimson+Text:ital@1&display=swap">
<style>
  :root {
    --bg-light: #f4f4f4;
    --bg-mid: #d9dadb;
    --bg-dark: #a9abad;
    --ink: #2a2a2c;
    --ink-soft: #3a3a3c;
    --thorn-dark: #4a3f36;
    --thorn-mid: #8a7a69;
    --horn-red: #8e1a1c;
  }
  html, body {
    margin: 0;
    padding: 0;
    overflow: hidden;
  }
  .cover {
    position: relative;
    width: 800px;
    height: 1200px;
    overflow: hidden;
    background:
      radial-gradient(ellipse 420px 460px at 50% 48%, var(--bg-light) 0%, rgba(244,244,244,0) 70%),
      linear-gradient(180deg, var(--bg-mid) 0%, #e6e7e8 40%, var(--bg-mid) 75%, var(--bg-dark) 100%);
    font-family: "Oswald", sans-serif;
    color: var(--ink);
  }
  .title {
    position: absolute;
    top: 40px;
    left: 0;
    width: 100%;
    margin: 0;
    text-align: center;
    font-weight: 600;
    text-transform: uppercase;
    line-height: 0.98;
  }
  .title-line {
    display: block;
    font-size: 118px;
    letter-spacing: 6px;
  }
  .crown-art {
    position: absolute;
    left: 130px;
    top: 230px;
    width: 560px;
    height: 800px;
    border-radius: 50%;
    background:
      radial-gradient(ellipse 50% 50% at 50% 50%,
        rgba(74,63,54,0) 0%,
        rgba(74,63,54,0) 52%,
        rgba(138,122,105,0.55) 62%,
        rgba(74,63,54,0.75) 72%,
        rgba(138,122,105,0.4) 84%,
        rgba(74,63,54,0) 100%);
  }
  .horn {
    position: absolute;
    top: 230px;
    width: 0;
    height: 0;
  }
  .subtitle {
    position: absolute;
    top: 530px;
    left: 0;
    width: 100%;
    margin: 0;
    text-align: center;
    font-family: "Crimson Text", serif;
    font-style: italic;
    font-size: 31px;
    line-height: 1.22;
    color: var(--ink-soft);
  }
  .author {
    position: absolute;
    bottom: 52px;
    left: 0;
    width: 100%;
    margin: 0;
    text-align: center;
    font-weight: 400;
    font-size: 42px;
    letter-spacing: 5px;
    text-transform: uppercase;
    color: var(--ink);
  }
</style>
</head>
<body>
  <main class="cover">
    <h1 class="title">
      <span class="title-line">Roaming</span>
      <span class="title-line">Quartets</span>
    </h1>

    <div class="crown-art" role="img" aria-label="Illustration of a floating ring of twisted thorny branches with two red horns rising from its upper edge"></div>

    <p class="subtitle">
      The Curious<br>
      Habits of<br>
      Norway's Traveling<br>
      Fiddlers<br>
      and Their Seaside<br>
      Rivals
    </p>

    <p class="author">Dorian Whitlock</p>
  </main>
</body>
</html>
```